Real Estate Company / Capital Needs Cards!

need business cards designed using the logos that were just designed by sketchhive.

Reason: per designers request deadline extended 1 day…thank you.

Target Market(s)

Investors and clients looking to purchase real estate or invest in the business.

Industry/Entity Type

Business

Requirements
Must have
• two designs - one for the real estate logo and one for the capital logo, similar but slightly different.
Nice to have
• something to make it pop (perhaps on the back)
Should not have
• much color

```html
<!DOCTYPE html>
<html lang="en">
<head>
<meta charset="utf-8">
<title>Veral Business Cards</title>
<link rel="stylesheet" href="https://fonts.googleapis.com/css2?family=Questrial&family=Crimson+Text:wght@600&family=Cinzel:wght@400&family=PT+Sans:ital@0;1&display=swap">
<style>
  :root {
    --page: #ececec;
    --label: #1c1c1c;
    --navy: #23262f;
    --black: #0d0d0d;
    --grey-dark: #4a4a4e;
    --grey-mid: #6a6869;
    --white: #ffffff;
    --ink: #1a1a1a;
    --ink-soft: #4a4a4a;
    --silver: #d9d6d0;
    --gold: #d8d0bd;
    --edge: #1a1a1a;
  }
  * { margin: 0; padding: 0; box-sizing: border-box; }
  html, body { width: 1200px; height: 1000px; overflow: hidden; }
  body { background: var(--page); position: relative; font-family: "PT Sans", sans-serif; }

  .side-label {
    position: absolute; top: 84px; font-family: "Questrial", sans-serif;
    font-size: 42px; color: var(--label); width: 566px; text-align: center;
  }
  .side-label--front { left: 26px; }
  .side-label--back { left: 606px; }

  .card { position: absolute; width: 566px; height: 324px; overflow: hidden; }
  .card--row1 { top: 159px; }
  .card--row2 { top: 531px; }
  .card--front { left: 26px; }
  .card--back { left: 606px; }

  .card--estate-front { background: linear-gradient(180deg, #262a34, var(--navy)); }
  .card--capital-front { background: radial-gradient(ellipse at 50% 40%, #3a3a3a 0%, #161616 55%, var(--black) 100%); }

  .brand { position: absolute; font-family: "Cinzel", serif; text-align: center; }
  .brand--estate { left: 0; right: 0; top: 112px; color: var(--silver); }
  .brand--estate .brand-name { font-size: 52px; line-height: 1; letter-spacing: 2px; }
  .brand--estate .brand-sub { font-size: 20px; letter-spacing: 4px; margin-top: 6px; }

  .brand-mark { position: absolute; left: 229px; top: 72px; width: 107px; height: 107px; background: var(--gold); border-radius: 8px; }
  .brand--capital { left: 0; right: 0; top: 192px; color: var(--gold); }
  .brand--capital .brand-name { font-size: 44px; line-height: 1; letter-spacing: 2px; }
  .brand--capital .brand-sub { font-size: 16px; letter-spacing: 3px; margin-top: 2px; }

  .back-panel { position: absolute; left: 0; top: 0; width: 311px; height: 324px; border-right: 2px solid var(--edge); }
  .card--row1 .back-panel { background: var(--grey-dark); }
  .card--row2 .back-panel { background: var(--grey-mid); }
  .back-info { position: absolute; left: 313px; top: 0; right: 0; bottom: 0; background: var(--white); }

  .holder { position: absolute; left: 0; width: 311px; top: 136px; text-align: center; }
  .holder-name { font-family: "Crimson Text", serif; font-weight: 600; font-size: 29px; color: var(--white); line-height: 1; }
  .holder-role { font-family: "PT Sans", sans-serif; font-style: italic; font-size: 16px; color: #e6e6e6; margin-top: 2px; }

  .contact { position: absolute; left: 18px; top: 46px; color: var(--ink-soft); font-size: 18px; }
  .contact-group { margin-bottom: 10px; }
  .contact-head { display: flex; align-items: center; gap: 8px; color: var(--ink); font-size: 18px; line-height: 22px; }
  .contact-head svg { width: 22px; height: 22px; fill: var(--ink); }
  .contact-line { line-height: 24px; }
</style>
</head>
<body>
  <div class="side-label side-label--front">Front</div>
  <div class="side-label side-label--back">Back</div>

  <section class="card card--front card--row1 card--estate-front">
    <div class="brand brand--estate">
      <div class="brand-name">VERAL</div>
      <div class="brand-sub">REAL ESTATE</div>
    </div>
  </section>

  <section class="card card--back card--row1">
    <div class="back-panel">
      <div class="holder">
        <div class="holder-name">Dalton Pryce</div>
        <div class="holder-role">MANAGER</div>
      </div>
    </div>
    <div class="back-info">
      <div class="contact">
        <div class="contact-group">
          <div class="contact-head"><svg viewBox="0 0 24 24"><path d="M12 2a7 7 0 0 0-7 7c0 5 7 13 7 13s7-8 7-13a7 7 0 0 0-7-7zm0 9.5A2.5 2.5 0 1 1 12 6.5a2.5 2.5 0 0 1 0 5z"/></svg>Adress</div>
          <div class="contact-line">1520 W. Orchard Ave</div>
          <div class="contact-line">Fairview, CA 90412</div>
        </div>
        <div class="contact-group">
          <div class="contact-head"><svg viewBox="0 0 24 24"><path d="M3 8c0-2 4-4 9-4s9 2 9 4v2h-5V8H8v2H3zM6 11h12l2 9H4zm6 2.5a2.5 2.5 0 1 0 0 5 2.5 2.5 0 0 0 0-5z"/></svg>Mob/Tel</div>
          <div class="contact-line">(555) 014-2208</div>
          <div class="contact-line">(555) 017-6631</div>
        </div>
        <div class="contact-group">
          <div class="contact-head"><svg viewBox="0 0 24 24"><path d="M2 5h20v14H2zm2 2v.5l8 5.5 8-5.5V7z"/></svg>Mail/Web</div>
          <div class="contact-line">hello@veralcap.com</div>
          <div class="contact-line">veralcap.com</div>
        </div>
      </div>
    </div>
  </section>

  <section class="card card--front card--row2 card--capital-front">
    <div class="brand-mark"></div>
    <div class="brand brand--capital">
      <div class="brand-name">VERAL</div>
      <div class="brand-sub">CAPITAL, LLC</div>
    </div>
  </section>

  <section class="card card--back card--row2">
    <div class="back-panel">
      <div class="holder">
        <div class="holder-name">Dalton Pryce</div>
        <div class="holder-role">MANAGER</div>
      </div>
    </div>
    <div class="back-info">
      <div class="contact">
        <div class="contact-group">
          <div class="contact-head"><svg viewBox="0 0 24 24"><path d="M12 2a7 7 0 0 0-7 7c0 5 7 13 7 13s7-8 7-13a7 7 0 0 0-7-7zm0 9.5A2.5 2.5 0 1 1 12 6.5a2.5 2.5 0 0 1 0 5z"/></svg>Adress</div>
          <div class="contact-line">1520 W. Orchard Ave</div>
          <div class="contact-line">Fairview, CA 90412</div>
        </div>
        <div class="contact-group">
          <div class="contact-head"><svg viewBox="0 0 24 24"><path d="M3 8c0-2 4-4 9-4s9 2 9 4v2h-5V8H8v2H3zM6 11h12l2 9H4zm6 2.5a2.5 2.5 0 1 0 0 5 2.5 2.5 0 0 0 0-5z"/></svg>Mob/Tel</div>
          <div class="contact-line">(555) 014-2208</div>
          <div class="contact-line">(555) 017-6631</div>
        </div>
        <div class="contact-group">
          <div class="contact-head"><svg viewBox="0 0 24 24"><path d="M2 5h20v14H2zm2 2v.5l8 5.5 8-5.5V7z"/></svg>Mail/Web</div>
          <div class="contact-line">hello@veralcap.com</div>
          <div class="contact-line">veralcap.com</div>
        </div>
      </div>
    </div>
  </section>
</body>
</html>
```